Packing for Razor Blade VORELIN

Dears: We need a packing design. The product is an Disposable Razor Blade. We are a company in Brazil.

The packing consists in a bag package which the Disposables Razos are placed. 5 units into each bag.

The bag is not 100% printed and should let a space to the customer see the razors inside. Some competitors uses oval circle. I attached competitor package (Tove Marigold)

The background color should be blue, this color tonality should vary its magnitude from dark blue to soft blue. Blue is a good color for personal care products because customer can take the impression of cleanness, especially for razor blade which has the fuction to shave.

You can feel free to add other colors however it can not be much colorfull because it may get trouble to printer company print it. Silver is good.

You can feel free to do details. You can feel free also to place the logo above the package or at bottom of it.

Dimmensions:
Heigh 24cm
Width 10cm

Featuring
- Featuring: Handle with Grip. In Portuguese - (Cabo Aderente)
- Featuring: 2 Razors. In portuguese - (Duas Lâminas)

Reason: I stayed many days with out providing feedbacks. I want to give more time for you .

Target Market(s)

Mans ( for woman we will design other package )

Requirements
Nice to have
• maybe some tears as a wet surface...
pls can feel free

```html
<!DOCTYPE html>
<html lang="pt">
<head>
<meta charset="utf-8">
<title>VORELIN — Embalagem Lâmina Descartável</title>
<link href="https://fonts.googleapis.com/css2?family=Cinzel:wght@400;600&family=Orbitron:wght@500&display=swap" rel="stylesheet">
<style>
  :root {
    --navy-deep: #010822;
    --navy: #031035;
    --blue-glow: #1f5fd6;
    --blue-mid: #3a78f0;
    --blue-soft: #6fa2ff;
    --silver: #e6eeff;
    --white: #ffffff;
  }
  html, body {
    margin: 0;
    padding: 0;
    width: 1200px;
    height: 2883px;
    overflow: hidden;
    background: var(--navy-deep);
  }
  .package {
    position: relative;
    width: 1200px;
    height: 2883px;
    overflow: hidden;
    background: radial-gradient(ellipse at 70% 35%, var(--navy) 0%, var(--navy-deep) 70%);
  }
  .light-artwork {
    position: absolute;
    left: 0;
    top: 380px;
    width: 1200px;
    height: 1420px;
    background:
      radial-gradient(ellipse 70% 40% at 45% 55%,
        rgba(255, 255, 255, 0.85) 0%,
        rgba(111, 162, 255, 0.7) 35%,
        rgba(31, 95, 214, 0.45) 60%,
        rgba(1, 8, 34, 0) 85%);
  }
  .brand {
    position: absolute;
    top: 255px;
    left: 0;
    width: 1100px;
    display: flex;
    justify-content: flex-end;
    align-items: center;
    gap: 30px;
  }
  .brand-dot {
    width: 44px;
    height: 44px;
    border-radius: 50%;
    background: var(--blue-glow);
  }
  .brand-name {
    font-family: "Orbitron", sans-serif;
    font-weight: 500;
    font-size: 124px;
    letter-spacing: 6px;
    color: var(--silver);
    line-height: 1;
  }
  .feature {
    position: absolute;
    margin: 0;
    font-family: "Cinzel", serif;
    font-weight: 400;
    font-size: 78px;
    letter-spacing: 2px;
    line-height: 1;
    color: var(--silver);
    text-shadow:
      0 0 6px var(--blue-soft),
      0 0 18px var(--blue-glow),
      0 0 36px var(--blue-glow);
    white-space: nowrap;
  }
  .feature-blades { left: 148px; top: 2068px; }
  .feature-grip { left: 340px; top: 2262px; }
</style>
</head>
<body>
<main class="package">
  <div class="light-artwork" role="img" aria-label="Faixa de luz branca e azul curva atravessando a embalagem, com reflexo suave abaixo"></div>

  <header class="brand">
    <span class="brand-dot"></span>
    <span class="brand-name">VORELIN</span>
  </header>

  <p class="feature feature-blades">DUAS LAMINAS</p>
  <p class="feature feature-grip">CABO ADERENTE</p>
</main>
</body>
</html>
```